BLENDWELL natural skin care line needs a product labels and logo design

We need product labels designed for plant based multitasking products with customizable options They are simple basic products that can be mixed at home,used in a way thats is beyond their intended function delivering a unique benefits Our Personalized and seasonal beauty offers versatility We are introducing 4 basic products ,6 additives with botanical extracts that help balance,nourish ,protect correct,energies and revive the skin and 2 seasonal products . Our products will help people address their own skin concerns and provide longer shelf life /Our products are safe for the environment and skin health and we like to see clean and simple Eco Labels Labels - that should communicate fresh,simple,fewer ingredients multi purpose. easy to mix

Target Market(s)

35 and up

Logo Text

Customize it ... blend ... mix .... Doesn’t have to have a text .. ?

Font styles to use
Serif

Colors

Designer to choose only greyscale colors for use in the design.

Requirements
Must have
• Most importantly is to know is that there are 2 different set of products that can be used as they are or enhanced with the other botanical additives ..customizable
for the products to give impression that they go together
The first set are the Basics ... second set treatment essence .. I open for new names
Nice to have
• Simple one color design easy to remember clean organic fresh

```html
<!DOCTYPE html>
<html lang="en">
<head>
<meta charset="utf-8">
<title>Blendwell Natural Skin Care – Jar Label</title>
<link rel="stylesheet" href="https://fonts.googleapis.com/css2?family=Lora:wght@400;700&display=swap">
<style>
  :root {
    --page-bg: #e4e4e4;
    --label-white: #ffffff;
    --band-grey: #3c3c3c;
    --mid-grey: #8c8c8c;
    --soft-grey: #ececec;
    --ink: #1e1e1e;
    --body-text: #333333;
    --box-bg: rgba(255,255,255,0.92);
  }
  * { box-sizing: border-box; margin: 0; padding: 0; }
  html, body { width: 1200px; height: 960px; overflow: hidden; }
  body {
    background: var(--page-bg);
    font-family: "Lora", serif;
    color: var(--body-text);
    position: relative;
  }
  .label {
    position: absolute;
    left: 150px; top: 270px;
    width: 900px; height: 420px;
    background:
      radial-gradient(ellipse at 48% 15%, var(--soft-grey) 0%, rgba(236,236,236,0) 55%),
      linear-gradient(90deg, var(--label-white) 0%, var(--label-white) 55%, #e2e2e2 72%, var(--mid-grey) 100%);
    box-shadow: 0 6px 20px rgba(0,0,0,0.12);
    overflow: hidden;
  }
  .ingredients {
    position: absolute;
    left: 14px; top: 44px;
    width: 182px;
    text-align: right;
    font-size: 15px;
    line-height: 28px;
    color: var(--body-text);
  }
  .quality-band {
    position: absolute;
    left: 210px; top: 0;
    width: 54px; height: 300px;
    background: var(--band-grey);
    display: flex; align-items: center; justify-content: center;
  }
  .quality-band span {
    transform: rotate(-90deg);
    white-space: nowrap;
    color: var(--label-white);
    font-size: 22px;
    letter-spacing: 2px;
  }
  .brand {
    position: absolute;
    left: 264px; top: 96px;
    width: 390px;
    text-align: center;
  }
  .brand-dot {
    display: block;
    width: 92px; height: 92px;
    margin: 0 auto 20px;
    border-radius: 50%;
    background: var(--band-grey);
  }
  .brand-name {
    font-weight: 700;
    font-size: 42px;
    line-height: 50px;
    color: var(--ink);
    letter-spacing: 1px;
  }
  .brand-tagline {
    margin-top: 18px;
    font-size: 28px;
    line-height: 36px;
    color: var(--band-grey);
  }
  .net-weight {
    position: absolute;
    left: 300px; top: 358px;
    font-size: 28px;
    color: var(--band-grey);
  }
  .directions {
    position: absolute;
    left: 660px; top: 26px;
    width: 232px;
    color: var(--ink);
  }
  .directions h2 {
    font-weight: 400;
    font-size: 21px;
    margin-bottom: 12px;
  }
  .directions p {
    font-size: 16px;
    line-height: 24px;
  }
  .usage-box {
    position: absolute;
    left: 650px; top: 206px;
    width: 240px;
    padding: 12px 14px;
    background: var(--box-bg);
    border-radius: 12px;
    font-size: 16px;
    line-height: 24px;
    color: var(--ink);
  }
  .contact {
    position: absolute;
    left: 660px; top: 344px;
    font-size: 16px;
    line-height: 28px;
    color: var(--ink);
    list-style: none;
  }
  .contact li { display: flex; align-items: center; gap: 10px; }
  .contact svg { width: 16px; height: 16px; }
</style>
</head>
<body>
  <section class="label">
    <p class="ingredients">Caprylic Triglycerides, Ethoxydiglycol, Glycerin, Glabularia Extract, Squalane, Zingiber Root, Camellia Sinensis Leaf, Sodium Hyaluronate, Panax Ginseng Root, Methyl Taurate, Butylene Glycol, Fragrance.</p>

    <div class="quality-band"><span>PREMIER QUALITY</span></div>

    <div class="brand">
      <span class="brand-dot"></span>
      <div class="brand-name">BLENDWELL</div>
      <div class="brand-tagline">Natural Skin Care</div>
    </div>

    <div class="net-weight">15g</div>

    <div class="directions">
      <h2>How to use :</h2>
      <p>Apply to all areas of the body for firm, smooth skin. Apply after a shower. Perform a Body Wrap weekly.</p>
    </div>

    <div class="usage-box">Apply 1-2x daily on clean skin. It's that simple. The formula helps in reducing stretch marks.</div>

    <ul class="contact">
      <li>
        <svg viewBox="0 0 16 16" aria-hidden="true"><rect x="3" y="3" width="10" height="7" fill="none" stroke="#1e1e1e" stroke-width="1.4"/><rect x="1" y="11" width="14" height="2" fill="#1e1e1e"/></svg>
        www.blendandmix.com
      </li>
      <li>
        <svg viewBox="0 0 16 16" aria-hidden="true"><path d="M4 1.5l2.2 3-1.4 1.6c.9 2 2.2 3.3 4.1 4.1l1.6-1.4 3 2.2-1.3 2.6C7.5 13.4 2.6 8.5 1.4 3z" fill="#1e1e1e"/></svg>
        555-014-2290
      </li>
    </ul>
  </section>
</body>
</html>
```